Bright Ledger Path LLC Seminar Workbook Template

Our mission: Our mission is to provide students with amazing accounting literacy experiences in amazing learning environments so they can accomplish amazing career and business goals.
We would like to have a Microsoft Word template that we can use for all of our course content. We are profession; yet not stuffy. We teach a timeless subject; yet we are very modern.
Our logo is attached. We would like our logo or parts of our logo to be incorporated into the template (for example, perhaps the tagline is included in the bottom right corner). We have also attached a sample of a company's work. We do not like their design; but it's the kind of end product that we are interested in.
We are grateful for anyone who is interested in this project. Thank you for your help.

```html
<!DOCTYPE html>
<html lang="en">
<head>
<meta charset="utf-8">
<title>Bright Ledger Path LLC – Workbook Page: Decision 1</title>
<link href="https://fonts.googleapis.com/css2?family=Montserrat:wght@700&family=Poppins:wght@300;400;700&display=swap" rel="stylesheet">
<style>
  :root {
    --backdrop: #04a7ea;
    --paper: #f7f7f7;
    --band: #dfe9d5;
    --ink: #111111;
    --body-ink: #222222;
    --brand-blue: #1ba7e1;
    --brand-yellow: #f6b90f;
    --brand-green: #8cc63f;
    --brand-red: #ee1c1c;
    --white: #ffffff;
  }
  * { margin: 0; padding: 0; box-sizing: border-box; }
  html, body { width: 1070px; height: 1200px; overflow: hidden; }
  body { background: var(--backdrop); position: relative; font-family: "Poppins", sans-serif; }

  .workbook-page {
    position: absolute; left: 227px; top: 155px; width: 613px; height: 865px;
    background: var(--paper); overflow: hidden;
  }
  .accent-band { position: absolute; left: 30px; top: 0; width: 58px; height: 449px; background: var(--band); }

  .decision-label {
    position: absolute; left: 30px; top: 47px;
    font-family: "Montserrat", sans-serif; font-weight: 700; font-size: 28px; color: var(--brand-blue);
  }
  .brand-name {
    position: absolute; right: 68px; top: 52px;
    font-family: "Poppins", sans-serif; font-weight: 700; font-size: 17px; color: var(--brand-blue);
  }

  .section-title {
    position: absolute; left: 31px; top: 110px; width: 160px;
    font-weight: 700; font-size: 33px; line-height: 39px; color: var(--ink); letter-spacing: -0.3px;
  }
  .down-arrows { position: absolute; left: 106px; top: 318px; }

  .intro-copy {
    position: absolute; left: 198px; top: 121px; width: 356px;
    font-size: 10.4px; line-height: 16.6px; color: var(--body-ink);
  }
  .intro-copy p + p { margin-top: 8px; }

  .breakdown-title {
    position: absolute; left: 31px; top: 490px;
    font-weight: 700; font-size: 23px; color: var(--ink);
  }
  .pillar { position: absolute; top: 550px; }
  .pillar-number { font-weight: 700; font-size: 34px; line-height: 46px; }
  .pillar-rule { width: 80px; height: 3px; margin-top: 2px; }
  .pillar-label { margin-top: 24px; font-weight: 700; font-size: 18px; line-height: 28px; color: var(--ink); }
  .pillar--skills { left: 41px; }   .pillar--skills .pillar-number { color: var(--brand-blue); }   .pillar--skills .pillar-rule { background: var(--brand-blue); }
  .pillar--struggle { left: 192px; } .pillar--struggle .pillar-number { color: var(--brand-yellow); } .pillar--struggle .pillar-rule { background: var(--brand-yellow); }
  .pillar--profit { left: 333px; }  .pillar--profit .pillar-number { color: var(--brand-green); }  .pillar--profit .pillar-rule { background: var(--brand-green); }
  .pillar--joy { left: 467px; }     .pillar--joy .pillar-number { color: var(--brand-red); }     .pillar--joy .pillar-rule { background: var(--brand-red); }

  .tagline-seal {
    position: absolute; left: 327px; top: 785px; width: 150px; height: 150px; border-radius: 50%;
    background: var(--brand-green); color: var(--white); text-align: center;
    font-weight: 300; font-size: 14px; line-height: 22px; padding-top: 24px; letter-spacing: 0.5px;
  }
  .page-number { position: absolute; left: 548px; top: 816px; font-weight: 700; font-size: 16px; color: var(--ink); }
</style>
</head>
<body>
  <main class="workbook-page">
    <div class="accent-band"></div>
    <div class="decision-label">Decision 1</div>
    <div class="brand-name">Bright Ledger Path</div>

    <h1 class="section-title">What’s the topic of your course?</h1>

    <svg class="down-arrows" width="26" height="84" viewBox="0 0 26 84" aria-hidden="true">
      <polygon points="0,0 26,0 13,21" fill="#8cc63f"/>
      <polygon points="0,31 26,31 13,52" fill="#8cc63f"/>
      <polygon points="0,62 26,62 13,83" fill="#8cc63f"/>
    </svg>

    <section class="intro-copy">
      <p>One of the most powerful steps you can take right now to kickstart your sources creation journey is to get clear on your course topic. This one step will put everything… and I mean everything… into motion.</p>
      <p>At this point you might have a few ideas–or too many ideas—for your first course, or maybe you feel stuck because you don’t have any ideas that feel like they could be “the one.”</p>
      <p>No matter where you are right now, the following seven creative strategies will help you choose the perfect topic for your course – the topic you ideal potential customer genuinely wants and needs to learn, and the topic you are genuinely excited to teach (because you know it well and love to teach it!)</p>
      <p>Before we jump into the seven strategies, there’s one concept you need to understand that will hep you narrow down your topic quickly. Tour goal is to find the sweet spot: the intersection between your skills and know-how, a struggle or challenge your audience is facing (and will gladly pay for the solution), and a topic that truly lights you up.</p>
    </section>

    <h2 class="breakdown-title">Let’s break this down</h2>

    <div class="pillar pillar--skills">
      <div class="pillar-number">01</div><div class="pillar-rule"></div>
      <div class="pillar-label">Your Skills<br>and<br>Know-How</div>
    </div>
    <div class="pillar pillar--struggle">
      <div class="pillar-number">02</div><div class="pillar-rule"></div>
      <div class="pillar-label">Your<br>Audience’s<br>struggle<br>and<br>challenges</div>
    </div>
    <div class="pillar pillar--profit">
      <div class="pillar-number">03</div><div class="pillar-rule"></div>
      <div class="pillar-label">Your profit<br>potential</div>
    </div>
    <div class="pillar pillar--joy">
      <div class="pillar-number">04</div><div class="pillar-rule"></div>
      <div class="pillar-label">What<br>lights<br>you up</div>
    </div>

    <div class="tagline-seal">WE’RE<br>SURE OF IT</div>
    <div class="page-number">2</div>
  </main>
</body>
</html>
```